Shine Crew

I need a flyer and business cards to hand out at office buildings and country clubs introducing my new auto detailing business, SHINE CREW. Call or text 913-555-0147 for an appointment. Complete auto detailing done at their place or mine, and we offer pick -up and drop-off, if needed. I believe the flyer needs a car on it. Black, blue, and pink are my preferred colors. While you go about your day's business, whether playing 18 holes of golf or putting in 8 hours at the office, we will have your ride shining like a new penny when you're ready to roll!

```html
<!DOCTYPE html>
<html lang="en">
<head>
<meta charset="utf-8">
<title>Shine Crew – Auto Detailing Flyer</title>
<link href="https://fonts.googleapis.com/css2?family=Poppins:ital,wght@0,300;0,400;0,600;0,700;0,800;0,900;1,400;1,600;1,800;1,900&family=Great+Vibes&display=swap" rel="stylesheet">
<style>
  :root {
    --ink: #1c1c1e;
    --card-top: #3a3b3d;
    --card-bottom: #2a2b2d;
    --cyan: #00e1f5;
    --pink: #ec1ec4;
    --white: #ffffff;
    --muted: #d9d9d9;
  }
  * { box-sizing: border-box; margin: 0; padding: 0; }
  html, body { width: 870px; height: 1200px; overflow: hidden; background: var(--ink); }
  body { font-family: "Poppins", sans-serif; color: var(--white); }

  .flyer {
    position: relative; width: 870px; height: 1200px; overflow: hidden;
    background:
      radial-gradient(ellipse 280px 320px at 800px 0px, rgba(0,225,245,.95), rgba(0,225,245,0) 100%),
      radial-gradient(ellipse 300px 170px at 870px 1200px, rgba(236,30,196,.5), rgba(236,30,196,0) 100%),
      radial-gradient(ellipse 260px 240px at 0 700px, rgba(0,180,210,.3), rgba(0,180,210,0) 100%),
      var(--ink);
  }
  .abs { position: absolute; }

  /* brand */
  .brand { left: 151px; top: 84px; display: flex; align-items: center; gap: 10px; }
  .brand-dot { width: 30px; height: 30px; border-radius: 50%; background: var(--cyan); }
  .brand-name { font-weight: 800; font-size: 28px; color: var(--cyan); }

  /* headline */
  .headline-band { left: 226px; top: 186px; height: 36px; padding: 0 14px; background: var(--pink);
    transform: skewX(-8deg); display: flex; align-items: center; z-index: 2;
    font-size: 28px; font-weight: 900; letter-spacing: 6px; color: var(--white); }
  .headline { left: 40px; top: 200px; width: 410px; text-align: center;
    font-weight: 900; font-size: 126px; line-height: 1; letter-spacing: -4px;
    background: linear-gradient(180deg, #e9f6fb 0%, var(--cyan) 55%, #0a8fe0 100%);
    -webkit-background-clip: text; background-clip: text; color: transparent; }

  /* photo areas */
  .photo { position: absolute; }
  .photo-hero { left: 449px; top: 166px; width: 421px; height: 266px;
    background: radial-gradient(ellipse at 60% 55%, #2f7fe6 0%, #1a5bc4 50%, rgba(26,91,196,0) 78%); }
  .photo-service { left: 0; top: 607px; width: 417px; height: 352px;
    background: radial-gradient(ellipse at 40% 60%, #b9bdc2 0%, #8e9398 35%, #2e6ed1 62%, rgba(30,90,200,0) 80%); }

  /* taglines */
  .tagline { left: 0; width: 478px; text-align: center; }
  .tag-lead { top: 362px; font-size: 19px; font-weight: 300; }
  .tag-lead b { font-weight: 800; font-style: italic; }
  .tag-vip { top: 380px; font-size: 40px; line-height: 1.15; font-weight: 900; font-style: italic; color: var(--pink); }
  .tag-any { top: 427px; font-size: 16px; font-weight: 800; font-style: italic; color: var(--cyan); }

  .pillars { left: 53px; top: 463px; width: 350px; height: 38px; display: flex; transform: skewX(-4deg); }
  .pillars span { flex: 1; display: flex; align-items: center; justify-content: center; text-align: center;
    font-size: 11.5px; font-weight: 800; font-style: italic; line-height: 1.1; color: var(--ink); }
  .pillars .p-cyan { background: var(--cyan); }
  .pillars .p-pink { background: var(--pink); color: var(--white); }

  .intro { left: 44px; top: 517px; width: 360px; text-align: center; }
  .intro h2 { font-size: 18px; font-weight: 800; font-style: italic; color: var(--cyan); white-space: nowrap; }
  .intro h2 em { color: var(--pink); }
  .intro p { margin: 4px auto 0; width: 330px; font-size: 10.5px; font-style: italic; line-height: 1.3; color: var(--muted); }

  /* offers */
  .offer-title { left: 498px; top: 452px; display: flex; align-items: baseline;
    font-size: 22px; font-weight: 400; font-style: italic; color: var(--cyan); white-space: nowrap; }
  .offer-title b { font-weight: 800; margin-left: 6px; }
  .offer-title .script { font-family: "Great Vibes", cursive; font-size: 48px; line-height: 1; color: var(--pink); font-style: normal; margin-left: 12px; }

  .card { position: absolute; width: 147px; height: 168px; border-radius: 14px;
    background: linear-gradient(180deg, var(--card-top), var(--card-bottom)); border: 1px solid rgba(0,225,245,.35); }
  .card .icon { position: absolute; left: 21px; top: 19px; width: 49px; height: 49px; border-radius: 50%; background: var(--cyan);
    display: flex; align-items: center; justify-content: center; }
  .card p { position: absolute; left: 21px; right: 8px; font-size: 13px; line-height: 1.23; font-weight: 400; color: var(--white); }
  .card p b { font-weight: 700; }
  .c1 { left: 498px; top: 516px; } .c1 p { top: 82px; }
  .c2 { left: 656px; top: 518px; } .c2 p { top: 85px; }
  .c3 { left: 498px; top: 696px; } .c3 p { top: 77px; }
  .c4 { left: 656px; top: 696px; } .c4 p { top: 78px; }

  .promise { left: 497px; top: 884px; width: 340px; }
  .promise h3 { font-size: 14px; font-weight: 800; font-style: italic; color: var(--cyan); white-space: nowrap; }
  .promise h3 em { color: var(--pink); }
  .promise p { margin-top: 5px; width: 300px; font-size: 11px; font-style: italic; line-height: 1.3; color: var(--muted); }

  /* before / after */
  .compare { position: absolute; top: 984px; width: 115px; height: 115px; border-radius: 50%; overflow: hidden;
    border: 2px solid var(--cyan); }
  .compare .label { position: absolute; left: 0; right: 0; bottom: 0; height: 22px; padding-top: 3px; text-align: center;
    font-size: 10.5px; font-weight: 600; font-style: italic; }
  .before .label { background: var(--cyan); color: var(--ink); }
  .after .label { background: var(--pink); color: var(--white); }
  .shot { width: 100%; height: 100%; }
  .red { background: radial-gradient(circle at 50% 65%, #c0392b 0%, #9e2a20 40%, #e9e9e9 75%); }
  .black { background: radial-gradient(circle at 50% 65%, #2b2d30 0%, #131416 45%, #eeeeee 78%); }
  .seat-dirty { background: radial-gradient(circle at 45% 50%, #c8c8c8 0%, #8d8d8d 55%, #3a3a3a 100%); }
  .seat-clean { background: radial-gradient(circle at 50% 50%, #f1efea 0%, #dedbd3 60%, #f7f7f7 100%); }

  /* contact */
  .cta { left: 53px; top: 1124px; display: flex; align-items: center; gap: 12px; font-weight: 700; font-size: 24px; line-height: 36px; white-space: nowrap; }
  .cta .call { color: var(--pink); }
  .cta .phone { color: var(--white); font-weight: 800; font-size: 25px; }
  .badge { left: 449px; top: 1123px; height: 29px; display: flex; font-size: 11.5px; font-weight: 700; transform: skewX(-4deg); white-space: nowrap; }
  .badge span { display: flex; align-items: center; padding: 0 12px; }
  .badge .b-cyan { background: var(--cyan); color: var(--ink); width: 141px; justify-content: center; }
  .badge .b-pink { background: var(--pink); color: var(--white); width: 211px; justify-content: center; }
</style>
</head>
<body>
<main class="flyer">
  <div class="abs brand"><span class="brand-dot"></span><span class="brand-name">Shine Crew</span></div>

  <div class="photo photo-hero" role="img" aria-label="Glossy blue sports car, front view with glowing headlight"></div>

  <div class="abs headline-band">SHINE</div>
  <h1 class="abs headline">CREW</h1>

  <div class="abs tagline tag-lead">WHERE YOUR <b>CAR GETS THE</b></div>
  <div class="abs tagline tag-vip">VIP TREATMENT</div>
  <div class="abs tagline tag-any">Anytime, anywhere!</div>

  <div class="abs pillars">
    <span class="p-cyan">FAST</span>
    <span class="p-pink">FRIENDLY</span>
    <span class="p-cyan">PROFESSIONAL<br>SERVICE</span>
  </div>

  <div class="abs intro">
    <h2>Showroom Shine, <em>Delivered to You!</em></h2>
    <p>Whether you're grinding through 8 hours at the office or hitting 18 holes on the course, we'll have your ride looking brand new by the time you're done.</p>
  </div>

  <div class="photo photo-service" role="img" aria-label="Silver SUV with open hood and a detailer in blue overalls standing beside it"></div>

  <div class="abs offer-title">WHAT<b>WE</b><span class="script">Offer</span></div>

  <div class="card c1">
    <div class="icon"><svg width="28" height="22" viewBox="0 0 28 22"><path d="M4 12 L7 5 H21 L24 12 V19 H4 Z" fill="var(--pink)"/><circle cx="9" cy="15" r="2" fill="var(--cyan)"/><circle cx="19" cy="15" r="2" fill="var(--cyan)"/></svg></div>
    <p>Complete<br><b>Interior &amp;<br>Exterior Auto<br>Detailing</b></p>
  </div>
  <div class="card c2">
    <div class="icon"><svg width="22" height="28" viewBox="0 0 22 28"><path d="M11 2 C5.5 2 3 6 3 10 C3 16 11 24 11 24 C11 24 19 16 19 10 C19 6 16.5 2 11 2 Z" fill="var(--pink)"/><circle cx="11" cy="10" r="3" fill="var(--cyan)"/><ellipse cx="11" cy="25" rx="8" ry="2" fill="none" stroke="var(--pink)" stroke-width="1.5"/></svg></div>
    <p>Service at<br><b>Your Place or<br>Ours</b></p>
  </div>
  <div class="card c3">
    <div class="icon"><svg width="32" height="20" viewBox="0 0 32 20"><path d="M2 6 H18 V15 H2 Z M18 9 H25 L29 13 V15 H18 Z" fill="var(--pink)"/><circle cx="8" cy="16" r="2.5" fill="var(--ink)"/><circle cx="24" cy="16" r="2.5" fill="var(--ink)"/></svg></div>
    <p><b>Pick-Up</b> &amp;<br><b>Drop-Off</b><br>Available</p>
  </div>
  <div class="card c4">
    <div class="icon"><svg width="30" height="30" viewBox="0 0 30 30"><circle cx="15" cy="15" r="11" fill="none" stroke="var(--pink)" stroke-width="3"/><text x="15" y="18.5" text-anchor="middle" font-family="Poppins, sans-serif" font-size="8.5" font-weight="800" fill="var(--pink)">24/7</text></svg></div>
    <p><b>Flexible<br>Hours</b> -By<br>Appointment<br>Only</p>
  </div>

  <div class="abs promise">
    <h3>We'll Make It Shine <em>Like a New Penny!</em></h3>
    <p>Trust SHINE CREW to treat your car like a masterpiece—because you deserve to drive clean.</p>
  </div>

  <div class="compare before" style="left:55px"><div class="shot red" role="img" aria-label="Dull red car side before polishing"></div><span class="label">Before</span></div>
  <div class="compare after" style="left:162px"><div class="shot red" role="img" aria-label="Glossy red car side after polishing"></div><span class="label">After</span></div>
  <div class="compare before" style="left:321px"><div class="shot black" role="img" aria-label="Damaged black car front before repair"></div><span class="label">Before</span></div>
  <div class="compare after" style="left:427px"><div class="shot black" role="img" aria-label="Restored black car front after repair"></div><span class="label">After</span></div>
  <div class="compare before" style="left:584px"><div class="shot seat-dirty" role="img" aria-label="Foam-covered car seat being cleaned"></div><span class="label">Before</span></div>
  <div class="compare after" style="left:689px"><div class="shot seat-clean" role="img" aria-label="Clean white leather car seats"></div><span class="label">After</span></div>

  <div class="abs cta">
    <span class="call">Call or Text</span>
    <svg width="22" height="22" viewBox="0 0 22 22"><circle cx="11" cy="11" r="9" fill="none" stroke="var(--cyan)" stroke-width="2.5"/><path d="M7.5 7 L9.5 6.5 L10.5 9 L9.3 10 C9.8 11.3 10.7 12.2 12 12.7 L13 11.5 L15.5 12.5 L15 14.5 C11 14.5 7.5 11 7.5 7 Z" fill="var(--cyan)"/></svg>
    <span class="phone">913-555-0147</span>
  </div>
  <div class="abs badge"><span class="b-cyan">Appointments only</span><span class="b-pink">We work around your schedule!</span></div>
</main>
</body>
</html>
```